QM_radiance is a new upcoming amazing brand for modesty women , which started in 2016.

Design a page with all products and stating the title of the collection and style of the products and pricing.
Will need to create a column of upcoming events as well for customer to keep updated of our sales or flea
Updates

Target Market(s)

Hijabista, modesttrend

Number of Pages Required

5+ page

Requirements
Nice to have
• About Us
• Our brand represents classy and elegance yet it is comfortable and conservative to be worn everyday.
• Designs, and colours of fabrics chiffon , silk crepe and sateen silks and viscose cotton are exclusively chosen by QMradiance, imported from mainly high quality materials and sent for self manufactured.
• InsyaAllah#QMradiance

```html
<!DOCTYPE html>
<html lang="en">
<head>
<meta charset="utf-8">
<title>QM Radiance</title>
<link href="https://fonts.googleapis.com/css2?family=Open+Sans:wght@400;600;700&family=Roboto+Slab:wght@400;500;700&display=swap" rel="stylesheet">
<style>
:root{
  --purple:#5a3c9e;
  --purple-dark:#4a2f88;
  --lavender:#e6e3f1;
  --ink:#333;
  --muted:#777;
  --navy:#16213a;
  --tile-dark:#333;
  --line:#e3e3e3;
  --footer:#f4f4f4;
  --star:#f2a81d;
}
*{margin:0;padding:0;box-sizing:border-box}
html,body{width:1200px;height:3087px;overflow:hidden}
body{position:relative;font-family:"Open Sans",Arial,sans-serif;color:var(--ink);background:#fff}
.abs{position:absolute}
.slab{font-family:"Roboto Slab",Georgia,serif}

/* top bar */
.topbar{left:0;top:0;width:1200px;height:41px;border-bottom:1px solid var(--line);font-size:10px;text-transform:uppercase;color:#555}
.topbar .lang{left:99px;top:14px}
.topbar .lang i{display:inline-block;width:12px;height:8px;background:#3b4f9a;margin-right:6px;vertical-align:middle}
.topbar .links{right:150px;top:0;display:flex;height:41px}
.topbar .links span{padding:0 20px;line-height:41px;border-left:1px solid var(--line)}
.cart{left:1066px;top:9px;width:24px;height:24px;border-radius:50%;background:var(--purple)}

/* hero */
.hero{left:0;top:41px;width:1200px;height:597px;background:linear-gradient(90deg,#dcd8ec,#ece9f5 60%,#e3e0ef)}
.hero-photo{left:597px;top:0;width:420px;height:597px;background:linear-gradient(180deg,#b7b2d3 0%,#5b4d98 25%,#2d2f4e 60%,#3a3c5c 100%);opacity:.85}
.logo{left:99px;top:41px;width:197px;height:54px;border:2px solid var(--purple);display:flex;align-items:center;justify-content:center;font-size:26px;color:var(--purple-dark);letter-spacing:.5px}
.nav{left:472px;top:44px;display:flex;gap:38px;font-size:15px;color:#333}
.nav .on{color:var(--purple)}
.nav svg{margin-top:3px}
.hero h1{left:158px;top:230px;font-size:44px;line-height:47px;color:var(--purple);font-weight:700}
.hero p{left:165px;top:337px;width:290px;font-size:14px;line-height:24px;color:#444}
.btn{left:167px;top:412px;width:140px;height:39px;background:var(--purple);color:#fff;font-size:13px;display:flex;align-items:center;justify-content:center;gap:8px}
.arrow{width:34px;height:34px;border-radius:50%;background:#9c9ca4;display:flex;align-items:center;justify-content:center}

/* category tiles */
.tile{top:679px;width:321px;height:237px}
.tile .ph{top:0;height:157px;width:105px}
.tile .label{left:0;top:157px;width:321px;height:80px;background:var(--tile-dark);color:#fff;font-size:19px;line-height:24px;padding:14px 18px;text-transform:uppercase}
.tile .label b{position:absolute;right:18px;top:26px;font-size:14px;text-decoration:underline;text-transform:none}

/* welcome */
.welcome{left:0;top:965px;width:1200px;text-align:center}
.welcome h2{font-size:32px;font-weight:400;color:#222}
.welcome h2 span{color:var(--purple)}
.welcome p{width:880px;margin:22px auto 0;font-size:11px;line-height:21px;color:#666}

/* section headings */
.sec-h{left:99px;font-size:25px;font-weight:400;color:#222}
.pager{left:1049px;display:flex;gap:4px}
.pager i{width:22px;height:22px;border:1px solid #888;border-radius:50%;display:flex;align-items:center;justify-content:center}

/* product cards */
.card{width:234px;border:1px solid var(--line);text-align:center}
.card .img{height:261px}
.card .name{margin-top:16px;font-size:15px;color:#555}
.card .meta{margin:8px 0 14px;font-size:13px;display:flex;justify-content:center;gap:28px;color:var(--purple)}
.stars{color:var(--star);letter-spacing:1px}
.stars s{text-decoration:none;color:#ccc}
.prod .img{height:180px}
.prod{border:none}
.prod .meta{margin-bottom:0}

/* features */
.features{left:0;top:1632px;width:1200px;height:325px;background:var(--navy)}
.feat{top:60px;width:300px;text-align:center;color:#fff}
.feat .circle{width:114px;height:114px;border:2px solid #fff;border-radius:50%;margin:0 auto;display:flex;align-items:center;justify-content:center}
.feat h3{margin-top:32px;font-size:16px;font-weight:700;text-transform:uppercase}
.feat p{margin-top:12px;font-size:11px;line-height:20px;font-weight:600;padding:0 20px}

/* blogs */
.blogs-h{left:0;top:2343px;width:1200px;text-align:center;font-size:30px;font-weight:400;color:#222}
.blogs-rule{left:565px;top:2391px;width:70px;height:2px;background:var(--purple)}
.blog-img{top:2428px;width:261px;height:258px}
.blog-box{top:2450px;width:250px;background:#fff;padding:14px 0 0 14px}
.blog-box h4{font-size:14px;line-height:22px;font-weight:400;color:#333;text-transform:uppercase}
.blog-box .date{margin-top:14px;font-size:12px;font-style:italic;color:var(--purple);display:flex;gap:24px}
.blog-box .date em{color:#555}
.blog-box p{margin-top:12px;font-size:11px;line-height:20px;color:#666}

/* footer */
.edge{left:0;top:2740px;width:1200px;height:10px;background:#e8dcc4}
.footer{left:0;top:2750px;width:1200px;height:275px;background:var(--footer)}
.footer h5{font-size:17px;font-weight:400;color:#222;margin-bottom:14px}
.fcol{top:45px}
.fcol p,.fcol li{font-size:11px;line-height:21px;color:#555;list-style:none}
.newsletter{left:99px;width:264px}
.newsletter p{text-align:justify}
.field{height:42px;background:#fff;border:1px solid var(--line);font-size:11px;padding:13px 14px}
.field-name{width:264px;margin-top:16px}
.email-row{display:flex;margin-top:12px;width:264px}
.field-email{width:165px}
.sub{width:99px;height:42px;background:var(--purple);color:#fff;font-size:12px;display:flex;align-items:center;justify-content:center}
.contact-row{display:flex;gap:16px;margin-bottom:14px;font-size:12px;color:#555;line-height:20px}
.contact-row svg{flex:none;margin-top:2px}
.socials{display:flex;gap:8px;margin-top:6px}
.socials i{width:25px;height:25px;display:block}
.bottom{left:0;top:3025px;width:1200px;height:62px;background:#111;color:#ddd;font-size:11px;text-align:center;line-height:62px}
</style>
</head>
<body>

<header class="abs topbar">
  <div class="abs lang"><i></i>English &#9662;</div>
  <div class="abs links"><span>Login &amp; Register</span><span>My Account</span><span>EUR $ &#9662;</span></div>
  <div class="abs cart"></div>
</header>

<section class="abs hero">
  <div class="abs hero-photo" role="img" aria-label="Model wearing a purple hijab and a sequined dark dress, with a faded echo behind her"></div>
  <div class="abs logo">QM RADIANCE</div>
  <nav class="abs nav">
    <span class="on">Home</span><span>Collections</span><span>Our Shop</span><span>Products</span><span>Blog</span><span>Contact</span>
    <svg width="14" height="14" viewBox="0 0 14 14"><circle cx="6" cy="6" r="4.5" fill="none" stroke="#333" stroke-width="2"/><line x1="9.5" y1="9.5" x2="13" y2="13" stroke="#333" stroke-width="2"/></svg>
  </nav>
  <h1 class="abs slab">SPARKLE<br>COLLECTION</h1>
  <p class="abs">Lorem ipsum dolor sit amet, consectetur adipiscing elit, tempor incididunt</p>
  <div class="abs btn">SHOP NOW <svg width="14" height="14" viewBox="0 0 14 14"><circle cx="7" cy="7" r="7" fill="#fff"/><path d="M5.5 4l3 3-3 3" fill="none" stroke="#5a3c9e" stroke-width="2"/></svg></div>
  <div class="abs arrow" style="left:51px;top:291px"><svg width="10" height="12"><path d="M7 1L2 6l5 5" fill="none" stroke="#fff" stroke-width="2"/></svg></div>
  <div class="abs arrow" style="left:1119px;top:291px"><svg width="10" height="12"><path d="M3 1l5 5-5 5" fill="none" stroke="#fff" stroke-width="2"/></svg></div>
</section>

<section>
  <div class="abs tile" style="left:99px">
    <div class="abs ph" style="left:0;background:linear-gradient(#dcdbe4,#5c3b60)" role="img" aria-label="Model in a plum hijab"></div>
    <div class="abs ph" style="left:108px;background:linear-gradient(#e0dde6,#b4206e)" role="img" aria-label="Model in a magenta hijab"></div>
    <div class="abs ph" style="left:216px;background:linear-gradient(#e3e0e8,#d86aa2)" role="img" aria-label="Model in a pink hijab"></div>
    <div class="abs label">Sparkle<br>Collection<b>Shop Now</b></div>
  </div>
  <div class="abs tile" style="left:440px">
    <div class="abs ph" style="left:0;background:linear-gradient(#e4e4ea,#d8d6e2)" role="img" aria-label="Model in a white hijab"></div>
    <div class="abs ph" style="left:108px;background:linear-gradient(#e2dde8,#c9a8d6)" role="img" aria-label="Model in a lilac hijab"></div>
    <div class="abs ph" style="left:216px;background:linear-gradient(#e2dde3,#9e1738)" role="img" aria-label="Model in a crimson hijab"></div>
    <div class="abs label">Flower Beads<br>Collection<b>Shop Now</b></div>
  </div>
  <div class="abs tile" style="left:780px">
    <div class="abs ph" style="left:0;background:linear-gradient(#dfdfe2,#6c6a1c)" role="img" aria-label="Model in an olive hijab"></div>
    <div class="abs ph" style="left:108px;background:linear-gradient(#dfe0e2,#1f5b45)" role="img" aria-label="Model in a green hijab"></div>
    <div class="abs ph" style="left:216px;background:linear-gradient(#e0e2e4,#5a9f94)" role="img" aria-label="Model in a teal hijab"></div>
    <div class="abs label">Crystalline<br>Collection<b>Shop Now</b></div>
  </div>
</section>

<section class="abs welcome">
  <h2 class="slab">WELCOME TO <span>QM RADIANCE</span></h2>
  <p>Lorem ipsum dolor sit amet, consectetur adipiscing elit, sed do eiusmod tempor incididunt ut labore et dolore magna aliqua. Ut enim ad minim veniam, quis nostrud exercitation ullamco laboris nisi ut aliquip ex ea commodo consequat. Duis aute irure dolor in reprehenderit in voluptate velit esse cillum dolore eu fugiat nulla pariatur. Excepteur sint occaecat cupidatat non proident, sunt in culpa qui officia deserunt mollit anim id est laborum</p>
</section>

<h2 class="abs sec-h slab" style="top:1172px">OUR COLLECTION</h2>
<div class="abs pager" style="top:1177px"><i><svg width="6" height="8"><path d="M5 1L1 4l4 3" fill="none" stroke="#555"/></svg></i><i><svg width="6" height="8"><path d="M1 1l4 3-4 3" fill="none" stroke="#555"/></svg></i></div>

<div class="abs card" style="left:99px;top:1225px"><div class="img" style="background:linear-gradient(#e2e2ea,#1c1c24)" role="img" aria-label="Model in a black hijab"></div><div class="name">Nemo enim ipsam volup</div><div class="meta"><span class="stars">★★★<s>★★</s></span><span>£255.99</span></div></div>
<div class="abs card" style="left:354px;top:1225px"><div class="img" style="background:linear-gradient(#e4e2e8,#f0b8a0)" role="img" aria-label="Model in a peach floral hijab"></div><div class="name">Nemo enim ipsam volup</div><div class="meta"><span class="stars">★★★<s>★★</s></span><span>£255.99</span></div></div>
<div class="abs card" style="left:609px;top:1225px"><div class="img" style="background:linear-gradient(#e2e2e8,#3c2a40)" role="img" aria-label="Model in a polka dot hijab"></div><div class="name">Nemo enim ipsam volup</div><div class="meta"><span class="stars">★★★<s>★★</s></span><span>£255.99</span></div></div>
<div class="abs card" style="left:864px;top:1225px"><div class="img" style="background:linear-gradient(#e2e3e4,#6b6a16)" role="img" aria-label="Model in an olive satin hijab"></div><div class="name">Nemo enim ipsam volup</div><div class="meta"><span class="stars">★★★<s>★★</s></span><span>£255.99</span></div></div>

<section class="abs features">
  <div class="abs feat" style="left:93px">
    <div class="circle"><svg width="56" height="40" viewBox="0 0 56 40" fill="none" stroke="#fff" stroke-width="3"><rect x="14" y="8" width="24" height="20"/><path d="M38 14h9l6 7v7H38"/><circle cx="22" cy="32" r="4" fill="#fff"/><circle cx="45" cy="32" r="4" fill="#fff"/><circle cx="12" cy="14" r="9" fill="#16213a"/><path d="M12 9v5h4"/></svg></div>
    <h3>Free Shipping</h3><p>We dispatch orders worldwide from our state of the art UK distribution centre</p>
  </div>
  <div class="abs feat" style="left:447px">
    <div class="circle"><svg width="40" height="40" viewBox="0 0 40 40" fill="#fff"><rect x="4" y="18" width="7" height="18"/><path d="M14 18l8-14c3 0 4 2 3 6l-1 6h11c2 0 3 2 2 4l-4 14c-1 2-2 2-4 2H14z"/></svg></div>
    <h3>Satisfaction 100% Guaranteed</h3><p>We dispatch orders worldwide from our state of the art UK distribution centre</p>
  </div>
  <div class="abs feat" style="left:809px">
    <div class="circle"><svg width="44" height="38" viewBox="0 0 44 38" fill="#fff"><path d="M6 20V10h24V3l10 10-10 10v-7H12v4z"/><path d="M38 18v10H14v7L4 25l10-10v7h18v-4z"/></svg></div>
    <h3>14 Day Easy Return</h3><p>We dispatch orders worldwide from our state of the art UK distribution centre</p>
  </div>
</section>

<h2 class="abs sec-h slab" style="top:2004px">OUR PRODUCT</h2>
<div class="abs pager" style="top:2009px"><i><svg width="6" height="8"><path d="M5 1L1 4l4 3" fill="none" stroke="#555"/></svg></i><i><svg width="6" height="8"><path d="M1 1l4 3-4 3" fill="none" stroke="#555"/></svg></i></div>

<div class="abs card prod" style="left:99px;top:2058px"><div class="img" style="background:linear-gradient(#e8ecee,#3fa596)" role="img" aria-label="Folded teal scarf with beads"></div><div class="name">Nemo enim ipsam volup</div><div class="meta"><span class="stars">★★★<s>★★</s></span><span>£255.99</span></div></div>
<div class="abs card prod" style="left:354px;top:2058px"><div class="img" style="background:linear-gradient(90deg,#f0c8c0,#b82838 45%,#3aa898)" role="img" aria-label="Row of hanging scarves in assorted colours"></div><div class="name">Nemo enim ipsam volup</div><div class="meta"><span class="stars">★★★<s>★★</s></span><span>£255.99</span></div></div>
<div class="abs card prod" style="left:609px;top:2058px"><div class="img" style="background:linear-gradient(90deg,#e8a0a8,#2a2e30 55%,#e8a848)" role="img" aria-label="Printed scarves laid out side by side"></div><div class="name">Nemo enim ipsam volup</div><div class="meta"><span class="stars">★★★<s>★★</s></span><span>£255.99</span></div></div>
<div class="abs card prod" style="left:864px;top:2058px"><div class="img" style="background:linear-gradient(#ecebed,#c29a90 50%,#e4d4c0)" role="img" aria-label="Stack of folded scarves in soft neutrals"></div><div class="name">Nemo enim ipsam volup</div><div class="meta"><span class="stars">★★★<s>★★</s></span><span>£255.99</span></div></div>

<h2 class="abs blogs-h slab">OUR BLOGS</h2>
<div class="abs blogs-rule"></div>

<div class="abs blog-img" style="left:99px;background:linear-gradient(90deg,#e8e6e4,#cc1c28 50%,#e6e4e2)" role="img" aria-label="Woman in a red sequined dress"></div>
<article class="abs blog-box" style="left:317px">
  <h4>Nemo enim ipsam voluptatem voluptas sit aspernatur</h4>
  <div class="date"><span>&#9638; March 25, 2016</span><em>&#9675; No comments</em></div>
  <p>Lorem ipsum dolor sit amet, consectetur adipiscing elit, sed do eiusmod tempor incididunt ut labore et dolore magna aliqua. Ut enim ad minim veniam.</p>
</article>
<div class="abs blog-img" style="left:626px;background:linear-gradient(90deg,#3a3230,#d8ccc4 50%,#40383a)" role="img" aria-label="Woman in a silver embellished gown by a doorway"></div>
<article class="abs blog-box" style="left:845px">
  <h4>Nemo enim ipsam voluptatem voluptas sit aspernatur</h4>
  <div class="date"><span>&#9638; March 25, 2016</span><em>&#9675; No comments</em></div>
  <p>Lorem ipsum dolor sit amet, consectetur adipiscing elit, sed do eiusmod tempor incididunt ut labore et dolore magna aliqua. Ut enim ad minim veniam.</p>
</article>

<div class="abs edge" role="img" aria-label="Decorative gold border strip"></div>
<footer class="abs footer">
  <div class="abs fcol newsletter">
    <h5 class="slab">Sign up for newsletter</h5>
    <p>Excepteur sint occaecat cupidatat non proident, sunt in culpa qui officia deserunt</p>
    <div class="field field-name">Enter Name</div>
    <div class="email-row"><div class="field field-email">Enter Email</div><div class="sub">SUBSCRIBE</div></div>
  </div>
  <div class="abs fcol" style="left:453px;width:260px">
    <h5 class="slab">Contacts Us</h5>
    <div class="contact-row"><svg width="12" height="16" viewBox="0 0 12 16"><path d="M6 0a6 6 0 0 1 6 6c0 4-6 10-6 10S0 10 0 6a6 6 0 0 1 6-6z" fill="#999"/><circle cx="6" cy="6" r="2" fill="#f4f4f4"/></svg><span>Harbour Lane, New South Wales<br>Australia</span></div>
    <div class="contact-row"><svg width="14" height="14" viewBox="0 0 14 14"><path d="M3 0l3 3-2 2c1 2 3 4 5 5l2-2 3 3-2 3C6 14 0 8 0 3z" fill="#999"/></svg><span>Phone: (02) 5550 1234</span></div>
    <div class="contact-row"><svg width="14" height="12" viewBox="0 0 14 12"><rect width="14" height="12" fill="#999"/><path d="M0 0l7 6 7-6" fill="none" stroke="#f4f4f4"/></svg><span>hello@qmradiance.example</span></div>
    <div class="socials"><i style="background:#dd4b39"></i><i style="background:#3b5998"></i><i style="background:#1da1f2"></i><i style="background:#0077b5"></i><i style="background:#e02a20"></i></div>
  </div>
  <div class="abs fcol" style="left:751px">
    <h5 class="slab">Customer Support</h5>
    <ul><li>Contact Us</li><li>Shipping &amp; Returns</li><li>Privacy Notice</li><li>Conditions of Use</li><li>My Account</li></ul>
  </div>
  <div class="abs fcol" style="left:998px">
    <h5 class="slab">My Account</h5>
    <ul><li>My Rewards</li><li>Register</li><li>About Rewards</li><li>Rewards FAQ</li><li>Rewards Terms</li><li>Sign In</li></ul>
  </div>
</footer>
<div class="abs bottom">©2015 - 2016 QM Radiance. All Rights Reserved.</div>

</body>
</html>
```